Quiet Lantern Cooperative branding package

We are looking for a branding package, including colors, fonts, and up to 10 graphics/icons to use across our materials (primarily on our website and in presentations). Ideally the branding package will align with our current logo, which is attached. The current colors are shades of yellow and green, which we'd like to see continued. Please help us identify one or two more complementary colors.

I am looking for graphics that create movement (spiral, arrow, etc), a sense of belonging (group of people, hands, tree, etc), an energetic environment (exclamation points, zig zags, etc), and peaceful environment (river, rocks, etc).

I prefer abstract and nature inspired graphics.

The graphics will be used for icons and graphics related to aging, public health, and equity. Other terms that will go with the icons include facilitation, interdisciplinary, collaboration, planning, and strategy.

Target Market(s)

Governmental public health, foundations, and other funders

Industry/Entity Type

Public health and consulting

Colors
59FF00
82FF00
B8FF75
E3FFCB
F4FFEA
FFC000
F8CF3A
FAE287
FDF2CF
FEFAEE
F0912C
F2A743
F7CA91
FBE8D2
FDF5EE

Requirements
Must have
• graphics that evoke feelings of movement, belonging, energetic, and peacefulness.
Nice to have
• Complementary colors for my logo
Should not have
• Feathers, hearts, and pineapples

```html
<!DOCTYPE html>
<html lang="en">
<head>
<meta charset="UTF-8">
<title>Quiet Lantern Cooperative — Brand Guide</title>
<link href="https://fonts.googleapis.com/css2?family=Oswald:wght@600&family=Oxygen:wght@700&family=Open+Sans:wght@400&family=Inter:wght@400&display=swap" rel="stylesheet">
<style>
  :root {
    --paper: #fefbf3;
    --ink: #231f20;
    --rule: #3a3a3a;
    --apple: #a7d786;
    --saffron: #f6c42b;
    --lavender: #9d46db;
    --icon-tone: #ece8dc;
  }
  html, body {
    margin: 0;
    padding: 0;
    overflow: hidden;
  }
  body {
    width: 845px;
    height: 1200px;
    background: var(--paper);
    color: var(--ink);
    font-family: "Inter", Arial, sans-serif;
    position: relative;
  }
  .rule {
    position: absolute;
    left: 49px;
    width: 744px;
    height: 0;
    border-top: 1px solid var(--rule);
  }
  .section-title {
    position: absolute;
    left: 49px;
    margin: 0;
    font-family: "Oswald", "Arial Narrow", sans-serif;
    font-weight: 600;
    font-size: 23px;
    line-height: 28px;
    display: flex;
    align-items: center;
    gap: 13px;
  }
  .section-title::before {
    content: "";
    width: 14px;
    height: 14px;
    border-radius: 50%;
    background: var(--ink);
  }
  .caption {
    position: absolute;
    left: 49px;
    margin: 0;
    font-size: 15px;
  }
  .swatch {
    position: absolute;
    top: 172px;
    width: 200px;
    text-align: center;
  }
  .swatch-dot {
    width: 77px;
    height: 77px;
    border-radius: 50%;
    margin: 0 auto 26px;
  }
  .swatch-name {
    font-size: 16px;
    margin: 0 0 5px;
  }
  .swatch-hex {
    font-size: 12px;
    margin: 0;
  }
  .divider {
    position: absolute;
    top: 176px;
    height: 153px;
    border-left: 1px solid var(--rule);
  }
  .type-display {
    position: absolute;
    left: 45px;
    top: 474px;
    margin: 0;
    font-family: "Oxygen", Arial, sans-serif;
    font-weight: 700;
    font-size: 64px;
    letter-spacing: -1px;
  }
  .type-body {
    position: absolute;
    left: 49px;
    top: 605px;
    margin: 0;
    font-family: "Open Sans", Arial, sans-serif;
    font-size: 29px;
  }
  .icon-grid {
    position: absolute;
    left: 55px;
    top: 752px;
    width: 735px;
    display: grid;
    grid-template-columns: repeat(5, 1fr);
    grid-auto-rows: 115px;
    gap: 12px 18px;
  }
  .icon-tile {
    background: var(--icon-tone);
    border-radius: 10px;
  }
</style>
</head>
<body>
  <div class="rule" style="top:66px"></div>
  <h2 class="section-title" style="top:74px">Color palette</h2>
  <div class="rule" style="top:109px"></div>
  <p class="caption" style="top:120px">Primary color palette</p>

  <div class="swatch" style="left:57px">
    <div class="swatch-dot" style="background:var(--apple)"></div>
    <p class="swatch-name">Granny Smith Apple</p>
    <p class="swatch-hex">HEX#&nbsp; a7d786</p>
  </div>
  <div class="divider" style="left:287px"></div>
  <div class="swatch" style="left:315px">
    <div class="swatch-dot" style="background:var(--saffron)"></div>
    <p class="swatch-name">Saffron</p>
    <p class="swatch-hex">HEX#&nbsp; f6c42b</p>
  </div>
  <div class="divider" style="left:543px"></div>
  <div class="swatch" style="left:557px">
    <div class="swatch-dot" style="background:var(--lavender)"></div>
    <p class="swatch-name">Lavender Indigo</p>
    <p class="swatch-hex">HEX#&nbsp; 9d46db</p>
  </div>

  <div class="rule" style="top:366px"></div>
  <h2 class="section-title" style="top:373px">Typography</h2>
  <div class="rule" style="top:408px"></div>

  <p class="caption" style="top:446px">Display: Oxygen Bold</p>
  <p class="type-display">HEADING</p>
  <p class="caption" style="top:575px">Body : Open Sans Regular</p>
  <p class="type-body">Heading</p>

  <div class="rule" style="top:687px"></div>
  <h2 class="section-title" style="top:694px">Icons Set (Style Sample)</h2>
  <div class="rule" style="top:729px"></div>

  <div class="icon-grid">
    <div class="icon-tile" role="img" aria-label="Hand-drawn arrow pointing right"></div>
    <div class="icon-tile" role="img" aria-label="Hand-drawn check mark in a circle"></div>
    <div class="icon-tile" role="img" aria-label="Hand-drawn handshake"></div>
    <div class="icon-tile" role="img" aria-label="Hand-drawn puzzle pieces"></div>
    <div class="icon-tile" role="img" aria-label="Hand-drawn rising bar chart with arrow"></div>
    <div class="icon-tile" role="img" aria-label="Hand-drawn curved return arrow"></div>
    <div class="icon-tile" role="img" aria-label="Hand-drawn infinity loop"></div>
    <div class="icon-tile" role="img" aria-label="Hand-drawn exclamation mark"></div>
    <div class="icon-tile" role="img" aria-label="Hand-drawn flowing waves"></div>
    <div class="icon-tile" role="img" aria-label="Hand-drawn rock"></div>
    <div class="icon-tile" role="img" aria-label="Hand-drawn arrow pointing left"></div>
    <div class="icon-tile" role="img" aria-label="Hand-drawn group of people"></div>
    <div class="icon-tile" role="img" aria-label="Hand-drawn four-way arrows"></div>
    <div class="icon-tile" role="img" aria-label="Hand-drawn tree"></div>
    <div class="icon-tile" role="img" aria-label="Hand-drawn reaching hands"></div>
  </div>
</body>
</html>
```